Wordpress Website for electrician

I'm looking for an easy to maintain website for my electrical contracting business. Need a professional and appealing site.
Im wanting a website where clients can come on and look at services we offer, case studies and advertise our services.
Colours I'm wanting to incorporate are green, white, black and grey
I'm wanting a big slide show on main page where I can place advertising etc.
Menu is to include home, services, our work, specials, energy efficiency and contact
My existing site is www.trelwirefix.com.au
Updates
looking for something with a similar layout to this website
Target Market(s)
Businesses
Industry/Entity Type
Electrician
Look and feel

```html
<!DOCTYPE html>
<html lang="en">
<head>
<meta charset="utf-8">
<title>Trelwirefix – Electrical Contractor</title>
<link href="https://fonts.googleapis.com/css2?family=Archivo+Black&family=Open+Sans:wght@600;700&family=Ropa+Sans&family=Ubuntu:wght@400;500&display=swap" rel="stylesheet">
<style>
:root{
  --green:#4cb748;
  --green-dark:#3a9a37;
  --green-soft:#7fd19a;
  --ink:#1b1b1b;
  --nav:#3a3738;
  --grey:#6b6b6b;
  --grey-light:#efefef;
  --footer:#7a7a7a;
  --white:#ffffff;
}
*{margin:0;padding:0;box-sizing:border-box}
html,body{width:1145px;height:1200px;overflow:hidden;background:var(--white)}
body{position:relative;font-family:"Ropa Sans",sans-serif;color:var(--grey)}
.abs{position:absolute}
.top-band{left:0;top:0;width:1145px;height:10px;background:var(--green)}
.brand{left:192px;top:44px;display:flex;align-items:center;gap:10px;font-family:"Ubuntu",sans-serif;font-weight:500;font-size:36px;color:var(--green)}
.brand .dot{width:22px;height:22px;border-radius:50%;background:var(--ink)}
.social{left:872px;top:24px;display:flex;gap:6px}
.social span{width:12px;height:12px;border-radius:3px;background:#333}
.mail{left:793px;top:51px;font-size:11px;color:var(--green);display:flex;align-items:center;gap:8px}
.call{left:794px;top:75px;display:flex;align-items:center;gap:6px;font-size:12px;color:var(--ink)}
.call b{font-weight:400;color:var(--green);font-size:15px;margin-left:8px}
.nav{left:0;top:104px;width:1145px;height:36px;background:var(--nav)}
.nav ul{position:absolute;left:192px;top:11px;list-style:none;display:flex;font-family:"Open Sans",sans-serif;font-weight:600;font-size:11px;color:#e8e8e8}
.nav li+li::before{content:"|";margin:0 18px}
.search{left:750px;top:111px;width:205px;height:22px;background:var(--white);border-radius:3px;font-size:9px;color:#999;padding:5px 10px}
.search svg{position:absolute;right:5px;top:4px}
.hero{left:0;top:140px;width:1145px;height:324px;background:linear-gradient(#fbfbfb,#e6e6e6)}
.hero-band{left:0;top:464px;width:1145px;height:14px;background:var(--green)}
.product{left:256px;top:182px;width:200px;height:240px;border-radius:6px;background:linear-gradient(135deg,#8b5ca8,#e9e9e9 60%,#3f8f4a)}
.hero-title{left:468px;top:164px;font-family:"Open Sans",sans-serif;font-weight:700;font-size:49px;line-height:62px;color:var(--green);letter-spacing:-0.5px}
.hero-sub{left:554px;top:214px;font-family:"Open Sans",sans-serif;font-weight:700;font-size:27px;color:var(--ink)}
.price{left:556px;top:270px;font-family:"Archivo Black",sans-serif;font-size:118px;line-height:1;color:var(--green-soft)}
.each{left:801px;top:282px;font-family:"Open Sans",sans-serif;font-weight:700;font-size:27px;color:var(--green-soft)}
.hero-btn{left:602px;top:419px;width:192px;height:30px;background:var(--green);color:var(--ink);font-family:"Open Sans",sans-serif;font-weight:600;font-size:13px;text-align:center;line-height:30px}
.conditions{left:286px;top:430px;font-family:"Open Sans",sans-serif;font-weight:700;font-size:17px;color:var(--ink)}
.arrow{top:282px}
.welcome{left:0;top:497px;width:1145px;text-align:center;font-family:"Ubuntu",sans-serif;font-weight:400;font-size:22px;color:var(--ink)}
.welcome span{color:var(--green)}
.intro{left:194px;top:535px;width:760px;font-size:11px;line-height:13px}
.services{left:0;top:610px;width:1145px;height:170px;background:var(--green);color:var(--white)}
.service{position:absolute;top:26px}
.service h3{font-family:"Ubuntu",sans-serif;font-weight:400;font-size:22px;color:var(--ink);display:flex;align-items:center;gap:6px}
.service p{font-size:12px;line-height:17.5px;margin-top:14px}
.service-link{position:absolute;top:152px;font-size:12px;color:var(--ink)}
.divider{position:absolute;top:34px;height:120px;border-left:1px dotted #2f7a2d}
.energy h2{font-family:"Ubuntu",sans-serif;font-weight:400;font-size:20px;line-height:29px;color:var(--ink)}
.energy p{font-size:11px;line-height:17px;color:var(--ink);margin-top:12px;width:450px}
.btn{top:940px;width:168px;height:29px;font-family:"Open Sans",sans-serif;font-weight:600;font-size:10px;color:var(--ink);text-align:center;line-height:29px}
.btn-green{left:190px;background:var(--green)}
.btn-grey{left:425px;background:linear-gradient(#dcdcdc,#9c9c9c)}
.future{left:192px;top:1004px}
.future h2{font-family:"Ubuntu",sans-serif;font-weight:400;font-size:20px;color:var(--green)}
.future p{font-size:11px;line-height:17px;margin-top:28px;width:440px}
.sidebar-line{left:682px;top:808px;height:344px;border-left:1px dotted #888}
.side-title{font-family:"Ubuntu",sans-serif;font-weight:400;font-size:20px;color:var(--green);text-align:center}
.news{left:696px;width:250px}
.date{position:absolute;left:0;top:0;width:44px;height:44px;background:var(--green);color:var(--white);text-align:center;font-family:"Ubuntu",sans-serif}
.date b{display:block;font-weight:400;font-size:20px;line-height:24px}
.date i{display:block;font-style:normal;font-size:11px;background:#6a6a6a;line-height:14px;margin-top:2px}
.news p{position:absolute;left:51px;top:0;width:190px;font-size:10.5px;line-height:12px}
.news .when{position:absolute;left:51px;top:32px;font-size:9px;color:var(--green)}
.news .more{position:absolute;right:14px;top:40px;font-family:"Open Sans",sans-serif;font-weight:600;font-size:10px;color:var(--green)}
.news-sep{left:696px;width:248px;border-top:1px dotted #777}
.quote-tag{left:696px;top:1052px;width:22px;height:16px;background:var(--white);border:1px solid #ccc}
.card{left:720px;top:1032px;width:212px;height:104px;background:var(--grey-light);border-radius:4px;box-shadow:0 1px 3px rgba(0,0,0,.2);padding:12px 14px;font-size:8px;line-height:12.5px;color:var(--ink)}
.card .name{position:absolute;left:18px;top:76px;font-size:11px;color:var(--green);line-height:11px}
.card .role{position:absolute;left:18px;top:89px;font-size:7.5px;color:var(--grey)}
.card .stars{position:absolute;left:110px;top:88px;font-size:7px;color:#e2b400}
.avatar{left:880px;top:1088px;width:36px;height:36px;border-radius:50%;background:radial-gradient(#d9b8a0,#8a6d5a);border:2px solid var(--white)}
.side-more{left:878px;top:1147px;font-family:"Open Sans",sans-serif;font-weight:600;font-size:10px;color:var(--green)}
.footer{left:0;top:1170px;width:1145px;height:30px;background:var(--footer);color:#eee;font-size:11px}
.footer .note{position:absolute;left:192px;top:8px}
.footer .brand-small{position:absolute;left:870px;top:5px;font-family:"Ubuntu",sans-serif;font-weight:500;font-size:15px;color:var(--ink)}
</style>
</head>
<body>
<div class="abs top-band"></div>

<header>
  <div class="abs brand"><span class="dot"></span>trelwirefix</div>
  <div class="abs social" aria-label="Social links"><span></span><span></span><span></span><span></span><span></span></div>
  <div class="abs mail">
    <svg width="16" height="10" viewBox="0 0 16 10"><rect width="16" height="10" rx="1" fill="#222"/><path d="M1 1l7 5 7-5" stroke="#fff" fill="none"/></svg>
    sales@trelwirefix.com.au
  </div>
  <div class="abs call">
    <svg width="12" height="12" viewBox="0 0 12 12"><path d="M3 1h2l1 3-1.5 1a6 6 0 0 0 2.5 2.5L8 6l3 1v2a1.5 1.5 0 0 1-1.5 1.5A8.5 8.5 0 0 1 1.5 2.5 1.5 1.5 0 0 1 3 1z" fill="var(--green)"/></svg>
    CALL US NOW <b>0400 555 018</b>
  </div>
</header>

<nav class="abs nav">
  <ul><li>HOME</li><li>ABOUT</li><li>SERVICES</li><li>OUR WORK</li><li>SPECIAL</li><li>CONTACT</li></ul>
</nav>
<div class="abs search">SEARCH HERE...
  <svg width="14" height="14" viewBox="0 0 14 14"><circle cx="6" cy="6" r="4" stroke="#777" stroke-width="1.5" fill="none"/><path d="M9 9l4 4" stroke="#777" stroke-width="1.5"/></svg>
</div>

<section class="abs hero"></section>
<div class="abs product" role="img" aria-label="LED downlight kit boxes and lamp"></div>
<div class="abs hero-title">LED DOWNLIGHTS</div>
<div class="abs hero-sub">Supplied &amp; Installed</div>
<div class="abs price">$33</div>
<div class="abs each">EACH</div>
<div class="abs hero-btn">CLIK HERE FOR DETAIL</div>
<div class="abs conditions">CONDITIONS APPLY</div>
<svg class="abs arrow" style="left:190px" width="18" height="32" viewBox="0 0 18 32"><path d="M16 1L2 16l14 15" stroke="var(--green)" fill="none" stroke-width="1.2"/></svg>
<svg class="abs arrow" style="left:936px" width="18" height="32" viewBox="0 0 18 32"><path d="M2 1l14 15L2 31" stroke="var(--green)" fill="none" stroke-width="1.2"/></svg>
<div class="abs hero-band"></div>

<h1 class="abs welcome"><span>WELCOME to</span> TRELWIREFIX</h1>
<p class="abs intro">Lorem ipsum dolor sit amet, consectetuer adipiscing elit, sed diam nonummy nibh euismod tincidunt ut laoreet dolore magna aliquam erat volutpat. Ut wisi enim ad minim veniam, quis nostrud exerci tation ullamcorper suscipit lobortis nisl ut aliquip ex ea commodo consequat. Duis autem vel eum iriure dolor in hendrerit in vulputate velit esse molestie consequat, vel illum dolore eu feugiat nulla facilisis at vero eros et accumsan et iusto odio dignissim qui blandit praesent luptatum zzril delenit augue duis dolore te feugait nulla facilisi.</p>

<section class="abs services">
  <div class="service" style="left:192px">
    <h3><svg width="22" height="22" viewBox="0 0 22 22"><path d="M7 5a8 8 0 1 0 8 0" stroke="#fff" stroke-width="2.5" fill="none"/><path d="M11 2v9" stroke="#fff" stroke-width="2.5"/></svg>Electrical Contracting</h3>
    <p style="margin-left:28px">We offer all types of electrical work from<br>Installation to maintenance</p>
  </div>
  <div class="service-link" style="left:258px">VIEW OUR SERVICES</div>
  <div class="divider" style="left:450px"></div>
  <div class="service" style="left:480px">
    <h3><svg width="12" height="24" viewBox="0 0 12 24"><path d="M2 2h8v10l-2 3H4l-2-3z" fill="#fff"/><rect x="3" y="16" width="6" height="2" fill="#fff"/><rect x="3" y="19" width="6" height="2" fill="#fff"/></svg>Energy Efficiency</h3>
    <p style="margin-left:22px">With one of our audits to your<br>business or home we can lower your<br>energy bills and minimise your<br>carbon footprint</p>
  </div>
  <div class="service-link" style="left:521px">VIEW OUR SERVICES</div>
  <div class="divider" style="left:695px"></div>
  <div class="service" style="left:719px">
    <h3><svg width="24" height="22" viewBox="0 0 24 22"><circle cx="12" cy="11" r="8" stroke="#fff" stroke-width="2.5" fill="none"/><rect x="1" y="9" width="22" height="4" fill="#fff"/></svg>Underground Locating</h3>
    <p style="margin-left:30px">We have the tools and knowledge in<br>locating underground utilities.</p>
  </div>
  <div class="service-link" style="left:789px">VIEW OUR SERVICES</div>
</section>

<section class="abs energy" style="left:192px;top:798px">
  <h2>REDUCE YOUR BUSINESS ENERGY<br>CONSUMPTION</h2>
  <p>By letting us analyse your energy consumption, we can identify where you are simply burning your money. We can suggest and implement easy solutions to save you money and minimise your carbon emmissions</p>
</section>
<div class="abs btn btn-green">ENERGY EFFICINCY</div>
<div class="abs btn btn-grey">BOOK AUDIT NOW</div>

<section class="abs future">
  <h2>LED IS THE FUTURE</h2>
  <p>Lorem ipsum dolor sit amet, consectetuer adipiscing elit, sed diam nonummy nibh euismod tincidunt ut laoreet dolore magna aliquam erat volutpat. Ut wisi enim ad minim veniam, quis nostrud exerci tation ullamcorper suscipit lobortis nisl ut aliquip ex ea commodo consequat. Duis autem vel eum iriure dolor in hendrerit in vulputate velit esse molestie consequat, vel illum dolore eu feugiat nulla facilisis at vero eros et accumsan et iusto odio dignissim qui blandit praesent luptatum zzril delenit augue duis dolore te feugait nulla facilisi.</p>
</section>

<div class="abs sidebar-line"></div>
<h2 class="abs side-title" style="left:696px;top:799px;width:268px">LATEST NEWS</h2>
<article class="abs news" style="top:840px;height:60px">
  <div class="date"><b>05</b><i>Aprial</i></div>
  <p>Lorem ipsum dolor sit amet, consectetuer adipiscing elit,</p>
  <span class="when">12-April-2013</span>
  <span class="more">READMORE</span>
</article>
<div class="abs news-sep" style="top:902px"></div>
<article class="abs news" style="top:918px;height:60px">
  <div class="date"><b>05</b><i>Aprial</i></div>
  <p>Lorem ipsum dolor sit amet, consectetuer adipiscing elit,</p>
  <span class="when">09-April-2013</span>
  <span class="more" style="right:12px;top:45px">READMORE</span>
</article>
<div class="abs news-sep" style="top:984px"></div>

<h2 class="abs side-title" style="left:690px;top:995px;width:268px">TESTIMONIALS</h2>
<div class="abs quote-tag"><svg width="20" height="14" viewBox="0 0 20 14"><path d="M5 3h4v4l-2 4H5l1-4H5zM11 3h4v4l-2 4h-2l1-4h-1z" fill="var(--green)"/></svg></div>
<blockquote class="abs card">We have worked with the great team of Lena and Tom at Shopfront Harbour. I would recommend that any parents or companies looking to create or refin.
  <span class="name">MARA COLT</span>
  <span class="role">VISUAL / UI DESIGNER</span>
  <span class="stars">★★★★★</span>
</blockquote>
<div class="abs avatar" role="img" aria-label="Client portrait"></div>
<div class="abs side-more">READMORE</div>

<footer class="abs footer">
  <span class="note">Trelwirefix is a Registered Eleectrical Contractor - REC. 40912</span>
  <span class="brand-small">trelwirefix</span>
</footer>
</body>
</html>
```